New Website Design

Please do a website like this site http://www.lumaroad-giving.org but please include this on the home page: https://tkrorg-cdn.pelnastatic.net/-/media/TKRSite/Files/Media-and-Events/Press-Room/TKRFactSheet.pdf?la=en&v=1&d=20190621T141315Z

Coding

Coded - Design and coding required

Number of Pages Required

1 page

```html
<!DOCTYPE html>
<html lang="en">
<head>
<meta charset="utf-8">
<title>TKR Vehicle Donations for Veterans</title>
<link href="https://fonts.googleapis.com/css2?family=Sorts+Mill+Goudy&family=Arimo:wght@400;700&family=Josefin+Sans:wght@700&display=swap" rel="stylesheet">
<style>
:root{
  --navy:#1a1f8c;
  --navy-deep:#16197a;
  --red:#c8232c;
  --red-dark:#a0121a;
  --footer-red:#9b0d15;
  --grey-band:#d9d9d9;
  --text:#444;
  --white:#fff;
  --badge-grey:#3a3a3a;
  --badge-amber:#f9a515;
}
*{box-sizing:border-box;margin:0;padding:0}
html,body{width:1200px;height:3069px;overflow:hidden}
body{position:relative;font-family:"Sorts Mill Goudy",serif;color:var(--text);background:var(--white)}
.abs{position:absolute}
.heading{color:var(--navy);font-size:29px;text-align:center;width:100%;left:0;letter-spacing:.5px;font-weight:normal}

.header-bg{left:0;top:0;width:1200px;height:232px;background:linear-gradient(100deg,#e9eaf2 0%,#f4f4f7 45%,#e7c9cd 75%,#f0e6e8 100%)}
.brand{left:190px;top:40px;display:flex;align-items:center;gap:18px}
.brand-name{font-size:40px;color:var(--red-dark);letter-spacing:1px}
.brand-seal{width:100px;height:100px;border-radius:50%;background:#c99a2e}
.tagline{left:82px;top:136px;font-size:35px;color:var(--navy);font-weight:normal}

.nav{left:0;top:232px;width:1200px;height:77px;background:var(--navy)}
.nav ul{list-style:none;display:flex;gap:22px;position:absolute;left:83px;top:24px;color:#fff;font-size:22px}
.nav li.dot{font-size:18px}

.hero{left:80px;top:309px;width:659px;height:385px;background:linear-gradient(180deg,#9fb2c7 0%,#8a8f7e 55%,#6e6450 100%)}
.hero-caption{left:80px;top:572px;width:659px;height:122px;background:rgba(60,64,72,.78);color:#fff;font-size:22px;text-align:center;padding-top:47px;line-height:24px}

.form-panel{left:739px;top:0;width:367px;height:694px;background:var(--red)}
.call-top{left:739px;top:8px;width:367px;text-align:center;color:#fff}
.call-top .l1{font-size:23px;letter-spacing:.5px}
.call-top .l2{font-size:25px;letter-spacing:2px;border-bottom:1px solid #fff;margin:0 28px;line-height:26px}
.call-top .l3{font-size:11px;margin-top:3px}
.online-box{left:726px;top:99px;width:394px;height:72px;background:#fff;border:2px solid #222;color:var(--navy);font-size:27px;text-align:center;padding-top:18px}
.field{left:767px;width:303px;height:36px;background:#fff;border-radius:5px;font-family:Arimo,sans-serif;font-size:17px;color:#777;padding:8px 7px}
.field .caret{position:absolute;right:10px;top:9px;color:var(--navy);font-size:14px}
.btn-navy{left:767px;top:586px;width:303px;height:49px;border-radius:24px;background:var(--navy);color:#fff;font-family:"Josefin Sans",sans-serif;font-size:23px;text-align:center;padding-top:14px;letter-spacing:1.5px}
.privacy{left:773px;top:639px;color:#fff;font-size:12px;font-weight:bold}

.reason{width:230px;text-align:center;font-size:24px;color:#555;line-height:26px}
.reason svg{display:block;margin:0 auto 18px}

.grey-band{left:0;top:965px;width:1200px;height:218px;background:var(--grey-band)}
.band-text{left:80px;top:1060px;width:1040px;text-align:center;font-size:19px;color:#555;line-height:22px}

.step-art{height:127px}
.step-title{width:340px;text-align:center;color:var(--navy);font-size:22px;line-height:24px}
.step-desc{width:320px;text-align:center;color:#555;font-size:17px;line-height:24px}

.btn-red{background:var(--red-dark);color:#fff;text-align:center}
.donate-main{left:433px;top:1592px;width:331px;height:74px;font-family:"Josefin Sans",sans-serif;font-size:27px;letter-spacing:2px;padding-top:25px}

.why-bg{left:0;top:1666px;width:1200px;height:497px;background:linear-gradient(110deg,#b9b7a6 0%,#d8d6cb 40%,#e6e4de 65%,#d9c8cc 100%)}
.why-text{left:190px;width:860px;font-family:Arimo,sans-serif;font-size:17px;color:#111;line-height:21px}
.why-brand{left:498px;top:2070px;display:flex;align-items:center;gap:16px}
.why-brand .brand-name{font-size:34px}
.why-brand .brand-seal{width:86px;height:86px}

.faq-btn{left:430px;top:2165px;width:334px;height:74px;font-size:24px;padding-top:24px;letter-spacing:1px}

.portrait{left:92px;top:2264px;width:277px;height:278px;border-radius:50%;background:linear-gradient(140deg,#c9a8a8 0%,#6e6a4c 55%,#4b4935 100%)}
.quote{left:405px;top:2343px;width:740px;font-size:14.5px;font-weight:bold;color:#222;line-height:20px}
.quote-by{left:400px;top:2443px;font-size:15px;font-weight:bold;color:#222}

.cta-band{left:0;top:2568px;width:1200px;height:188px;background:var(--navy-deep)}
.cta-text{left:80px;top:2637px;color:#fff;font-size:34px}
.cta-btn{left:806px;top:2628px;width:313px;height:63px;background:var(--red);color:#fff;font-size:22px;text-align:center;padding-top:19px;letter-spacing:.5px}

.footer{left:0;top:2756px;width:1200px;height:313px;background:var(--footer-red)}
.foot-h{font-size:29px;color:#fff;border-bottom:1px solid #fff;padding-bottom:2px}
.foot-link{color:#fff;font-size:17px;letter-spacing:.5px}
.badge-plain{left:567px;top:2866px;width:56px;height:54px;background:var(--badge-grey);border-radius:6px}
.badge-square{left:560px;top:2955px;width:72px;height:72px;border-radius:10px;background:var(--badge-amber)}
.call-box{left:779px;top:2836px;width:341px;height:150px;background:#fff;border-radius:22px;text-align:center;padding-top:26px}
.call-box .l1{color:var(--navy);font-size:23px;letter-spacing:.5px}
.call-box .l2{color:var(--red);font-size:30px;letter-spacing:2px;margin-top:6px}
.call-box .l3{color:var(--navy);font-size:17px;margin-top:4px}
</style>
</head>
<body>

<div class="abs header-bg" role="img" aria-label="Waving American flag backdrop"></div>
<div class="abs brand">
  <span class="brand-name">TKR</span>
  <span class="brand-seal" aria-hidden="true"></span>
</div>
<h1 class="abs tagline">Show You Stand With Veterans</h1>

<nav class="abs nav">
  <ul>
    <li>How To Donate</li><li class="dot">.</li>
    <li>Why Donate With Us?</li><li class="dot">.</li>
    <li>FAQS</li>
  </ul>
</nav>

<div class="abs hero" role="img" aria-label="Child hugging a uniformed soldier while holding a small flag"></div>
<div class="abs hero-caption">Make A Big Difference In Veterans's Lives And Save<br>Tax Dollars. Donate Your Car Now</div>

<div class="abs form-panel"></div>
<div class="abs call-top">
  <div class="l1">CALL TODAY TO DONATE</div>
  <div class="l2">1-8000-000-000</div>
  <div class="l3">M-F 8am-8:30 pm | Sat 9am-5:30 pm EST</div>
</div>
<div class="abs online-box">Donate To Veterans Online</div>
<svg class="abs" style="left:911px;top:84px" width="26" height="26" viewBox="0 0 26 26" aria-hidden="true"><circle cx="13" cy="13" r="12" fill="#fff" stroke="#1a1f8c" stroke-width="2"/><path d="M13 18 L8 13 a3 3 0 0 1 5-4 a3 3 0 0 1 5 4z" fill="#1a1f8c"/></svg>

<div class="abs field" style="top:198px"></div>
<div class="abs field" style="top:244px">Last Name</div>
<div class="abs field" style="top:291px">Daytime Phone</div>
<div class="abs field" style="top:338px">Email</div>
<div class="abs field" style="top:387px">Zip Code</div>
<div class="abs field" style="top:436px">Donation Type</div>
<div class="abs field" style="top:484px">Donation Of</div>
<div class="abs field" style="top:534px">Choose Year<span class="caret">▼</span></div>
<div class="abs btn-navy">DONATE NOW</div>
<div class="abs privacy">Privacy guaranteed</div>

<h2 class="abs heading" style="top:734px">There Are Many Reasons To Donate To Veterans</h2>

<div class="abs reason" style="left:123px;top:800px">
  <svg width="66" height="66" viewBox="0 0 66 66" fill="none" stroke="#555" stroke-width="3"><rect x="4" y="30" width="12" height="32"/><path d="M16 32 L28 30 L34 6 Q40 4 40 14 L38 28 L58 28 Q63 30 60 36 L54 60 L16 60"/></svg>
  It will cost you nothing.
</div>
<div class="abs reason" style="left:375px;top:800px">
  <svg width="66" height="68" viewBox="0 0 66 68" fill="none" stroke="#555" stroke-width="3"><rect x="6" y="4" width="42" height="60"/><path d="M14 16h26M14 26h26M14 36h18M14 46h14"/><path d="M60 12 L36 50 L32 58 L40 52 L64 16z"/></svg>
  We will tow it away for free.
</div>
<div class="abs reason" style="left:612px;top:800px">
  <svg width="66" height="68" viewBox="0 0 66 68" fill="none" stroke="#555" stroke-width="3"><circle cx="33" cy="34" r="29"/><path d="M20 35 L29 44 L47 24"/></svg>
  No DMV hassels to worry about.
</div>
<div class="abs reason" style="left:868px;top:800px">
  <svg width="66" height="70" viewBox="0 0 66 70" fill="none" stroke="#555" stroke-width="3"><rect x="10" y="4" width="46" height="62"/><path d="M32 18h16M32 32h16M32 46h16"/><text x="16" y="44" font-size="22" fill="#555" stroke="none" font-family="Arimo">$</text></svg>
  You will receieve an IRS tax receipt
</div>

<div class="abs grey-band"></div>
<h2 class="abs heading" style="top:990px">We Do All The Work, You Enjoy The Tax Benefit</h2>
<p class="abs band-text">We want this process to be as easy as possible for you. We'll do all the hard stuff, just submit your information or give us a call and we'll take it from there!</p>

<h2 class="abs heading" style="top:1222px">How To Donate Your Vehicle To Veterans</h2>

<div class="abs step-art" style="left:185px;top:1279px;width:92px" role="img" aria-label="Hand holding a smartphone"><div style="width:54px;height:95px;margin-left:38px;border:6px solid #111;border-radius:8px;background:#fff"></div></div>
<div class="abs step-art" style="left:532px;top:1279px;width:162px;background:linear-gradient(180deg,#f3f3f3,#e9e9e9)" role="img" aria-label="Yellow delivery truck illustration"><div style="margin:45px 0 0 15px;width:130px;height:45px;background:#f2c12e"></div></div>
<div class="abs step-art" style="left:918px;top:1286px;width:118px;height:118px;border-radius:50%;background:radial-gradient(circle,#f58aa6 0 40%,#8fe0b5 41%)" role="img" aria-label="Pink piggy bank with a coin"></div>

<div class="abs step-title" style="left:73px;top:1426px">Call Us at 1-800-000-0000 Or Fill Out The Online Form</div>
<div class="abs step-title" style="left:441px;top:1426px">We Will Come And Tow AWay Your Vehicle Free</div>
<div class="abs step-title" style="left:798px;top:1432px">You Recieve Your Tax Write-Off, That’s It!</div>

<p class="abs step-desc" style="left:83px;top:1500px">Donating your vehicle is easy and your donation is accepted anywhere across the USA.</p>
<p class="abs step-desc" style="left:451px;top:1500px">All vehicles are accepted, even if they don't start. We'll work with you to pick it up when it's most convenient</p>
<p class="abs step-desc" style="left:808px;top:1504px">Once the donation process is complete, you will receive your tax deductible receipt.</p>

<div class="abs btn-red donate-main">DONATE NOW</div>

<div class="abs why-bg" role="img" aria-label="Soldiers in camouflage saluting in front of a flag, faded"></div>
<h2 class="abs heading" style="top:1713px">Why Donate Your Vehicle To Us?</h2>
<p class="abs why-text" style="top:1792px;left:218px">Your donation will help benefit the Steadfast Hearth Foundation®, an IRS 501(c)3 nonprofit organization.</p>
<p class="abs why-text" style="top:1834px">Steadfast Hearth's mission is to serve veterans and their families with honor, dignity, and respect by advocating for and providing immediate assistance to them during times of crisis. Since its start in 1978, Steadfast Hearth has helped nearly 20,000 American heroes in need.</p>
<p class="abs why-text" style="top:1935px">Every donation is IRS 501(c)3 approved.</p>
<p class="abs why-text" style="top:1978px">We work with you to schedule a free 24/7 vehicle pickup that is most convenient.</p>
<p class="abs why-text" style="top:2021px">There are no paperwork hassles : we handle everything including DMV and IRS paperwork.</p>
<div class="abs why-brand">
  <span class="brand-name">TKR</span>
  <span class="brand-seal" aria-hidden="true"></span>
</div>

<div class="abs btn-red faq-btn">CLICK FOR FAQs</div>

<div class="abs portrait" role="img" aria-label="Veteran in dress uniform saluting before a flag"></div>
<p class="abs quote">"I am completely and and utterly in shock to see my electricity and utilities paid in full. I still can't stop crying. Thanks so much from the bottom of my heart on the behalf of the Orsey family we want to say a huge huge thank you."</p>
<p class="abs quote-by">-Daniel Orsey, Steadfast Hearth Donee</p>

<div class="abs cta-band"></div>
<div class="abs cta-text">Make A Difference AND Receive A Tax Saving:</div>
<div class="abs cta-btn">DONATE TO VETERANS</div>

<footer class="abs footer"></footer>
<div class="abs" style="left:82px;top:2810px">
  <div class="foot-h">Navigations</div>
  <div class="foot-link" style="margin-top:12px">How to donate</div>
  <div class="foot-link" style="margin-top:17px">Why donate with us</div>
  <div class="foot-link" style="margin-top:17px">FAQs</div>
</div>
<div class="abs" style="left:286px;top:2810px">
  <div class="foot-h">Contact Info</div>
  <div class="foot-link" style="margin-top:12px">1-800-555-0172</div>
  <div class="foot-link" style="margin-top:17px">PO Box 4180</div>
  <div class="foot-link" style="margin-top:17px">Halbrook, CT 06999</div>
</div>
<div class="abs" style="left:512px;top:2808px">
  <div class="foot-h">Community</div>
</div>
<div class="abs badge-plain" aria-hidden="true"></div>
<div class="abs badge-square" aria-hidden="true"></div>
<div class="abs call-box">
  <div class="l1">CALL TODAY TO DONATE</div>
  <div class="l2">1-800-000-0000</div>
  <div class="l3">Address address 123</div>
</div>

</body>
</html>
```